Corporate Website - KALDRA HOLDINGS, LLC

This Nevada Corporation has several subsidiaries:
T. M. Designs - Interior Design; Commercial, Residential & Hospitality
T. M. Style - Fashion Design & Styling
VERN LOUNGE - Upscale Membership Only Lounge servicing Business Men and women. It is located in Accra, Ghana
VERN SUITES - Full Service Executive Suites for top Businesses. Located in Accra, Ghana.
THE MATERIAL NOOK - Distributor for Building and Interior Design Materials
URL: www.kaldraholdingsllc.example
Website: info@kaldraholdingsllc.example
Phones: 1 702-555-0147 Las Vegas; +233 26 5550193 Ghana

Industry/Entity Type

Fashion

```html
<!DOCTYPE html>
<html lang="en">
<head>
<meta charset="utf-8">
<title>KALDRA HOLDINGS, LLC</title>
<link href="https://fonts.googleapis.com/css2?family=Open+Sans:ital,wght@0,400;0,600;0,700;1,400&family=Didact+Gothic&display=swap" rel="stylesheet">
<style>
:root{
  --teal:#1fc6b4;
  --teal-btn:#3cc7bc;
  --blue:#3d95e6;
  --band:#4b8fd0;
  --band-dark:#396f9f;
  --ink:#2b3138;
  --ink-soft:#4a5560;
  --grey-text:#9aa2a8;
  --offer-bg:#f5f5f5;
  --footer-bg:#4a5561;
  --white:#ffffff;
}
*{margin:0;padding:0;box-sizing:border-box}
html,body{width:1200px;height:2449px;overflow:hidden;background:var(--white)}
body{font-family:"Open Sans",Arial,sans-serif;color:var(--ink)}
.page{position:relative;width:1200px;height:2449px;overflow:hidden}
.abs{position:absolute}

/* hero */
.hero{left:0;top:0;width:1200px;height:588px;
  background:
    linear-gradient(90deg,rgba(120,80,50,.35) 0%,rgba(255,255,255,0) 30%,rgba(60,110,60,.35) 50%,rgba(255,255,255,0) 70%,rgba(120,80,50,.3) 100%),
    linear-gradient(180deg,#e6e3de 0%,#d9d3c9 30%,#b8a892 55%,#8b6a4c 78%,#6b4a30 100%)}
.site-header{left:80px;top:0;width:1042px;height:92px;background:var(--white)}
.brand{left:26px;top:14px;font-size:20px;color:#3a8fc9;font-weight:400}
.nav{left:380px;top:0;display:flex}
.nav-item{width:120px;text-align:center;padding-top:22px;font-size:14px;color:#55606a;position:relative}
.nav-item small{display:block;font-size:10px;font-style:italic;color:#9aa2a8;margin-top:2px}
.nav-item.active{color:var(--teal)}
.nav-item.active::before{content:"";position:absolute;left:10px;right:10px;top:0;height:3px;background:var(--teal)}
.search-btn{left:986px;top:30px;width:28px;height:28px;background:var(--teal);border-radius:3px}
.arrow{top:334px;width:36px;height:36px;border-radius:50%;background:rgba(40,40,40,.8)}

/* subsidiaries band */
.band{left:0;top:588px;width:1200px;height:106px;background:var(--band)}
.band-tab{top:0;width:208px;height:106px;text-align:center;color:var(--white);font-size:13px;font-weight:700;padding-top:22px}
.band-tab.current{background:var(--band-dark)}
.band-tab svg{display:block;margin:10px auto 0}

/* about */
.about-title{left:43px;top:704px;font-family:"Didact Gothic",sans-serif;font-size:22px;font-weight:700;color:#111;letter-spacing:.5px}
.about-text{left:63px;width:1000px;font-family:"Didact Gothic",sans-serif;font-size:17.5px;line-height:20.5px;color:#333}

/* offer */
.offer{left:0;top:939px;width:1200px;height:428px;background:var(--offer-bg)}
.offer-title{left:86px;top:50px;font-size:52px;font-weight:400;line-height:60px;color:var(--ink-soft)}
.offer-item{left:443px;width:640px}
.offer-icon{position:absolute;left:0;top:0;width:70px;height:70px;border-radius:50%;background:var(--blue)}
.offer-icon svg{position:absolute;left:22px;top:22px}
.offer-item h3{position:absolute;left:88px;top:8px;font-size:20px;font-weight:400;color:#444}
.offer-item p{position:absolute;left:88px;top:42px;font-size:13px;line-height:20px;color:var(--grey-text);width:540px}

/* contact */
.contact{left:0;top:1367px;width:1200px;height:780px;
  background:linear-gradient(180deg,#5f6c77 0%,#58656f 45%,#63707a 70%,#56636d 100%)}
.contact h2{position:absolute;left:0;width:1200px;text-align:center;color:var(--white);font-weight:400}
.contact-col{top:120px;width:340px;text-align:center;color:var(--white)}
.contact-col svg{display:block;margin:0 auto}
.contact-col .bar{width:60px;height:5px;background:var(--blue);margin:18px auto 0}
.contact-col h4{font-size:20px;font-weight:400;margin-top:14px}
.contact-col p{font-size:14px;margin-top:16px}
.btn{text-align:center;font-size:12px;font-weight:700;color:var(--white);text-transform:uppercase}
.btn-line{left:529px;top:433px;width:142px;height:37px;line-height:37px;background:var(--blue)}
.field{background:var(--white);border-radius:4px;font-size:12px;color:#9aa2a8;padding:12px 18px}
.btn-send{left:82px;top:650px;width:151px;height:40px;line-height:40px;background:var(--teal-btn);border-radius:3px}

/* footer */
.footer{left:0;top:2147px;width:1200px;height:302px;background:var(--footer-bg);color:var(--white)}
.footer h5{position:absolute;top:60px;font-size:18px;font-weight:400}
.footer h5 b{font-weight:700}
.news-text{left:82px;top:100px;width:480px;font-size:12.5px;line-height:20px;color:#8e99a3}
.news-input{left:82px;top:151px;width:224px;height:43px;background:var(--white);border-radius:3px;font-size:11px;font-style:italic;color:#9aa2a8;padding:14px 16px}
.news-btn{left:318px;top:151px;width:119px;height:43px;line-height:43px;background:var(--teal-btn);border-radius:3px}
.social{left:82px;top:248px;display:flex;gap:6px}
.social span{width:18px;height:18px;background:#5f6a75;border-radius:2px}
.menu a{position:absolute;font-size:12px;color:var(--white);text-decoration:none}
.tweet-dot{width:22px;height:22px;border-radius:50%;background:#2d9be8}
.tweet{left:918px;width:200px;font-size:11px;font-style:italic;line-height:17px;color:var(--white)}
</style>
</head>
<body>
<div class="page">

  <!-- hero -->
  <div class="abs hero" role="img" aria-label="Photo of a bright open-plan loft interior designed by T. M. Designs, with a bedroom, staircase, indoor planter and kitchen dining table"></div>
  <header class="abs site-header">
    <div class="abs brand">KALDRA HOLDINGS, LLC</div>
    <nav class="abs nav">
      <div class="nav-item active">Home<small>main page</small></div>
      <div class="nav-item">Pages<small>internal pages</small></div>
      <div class="nav-item">Services<small>what we offer</small></div>
      <div class="nav-item">Blog<small>our posts</small></div>
      <div class="nav-item">Contact<small>find us</small></div>
    </nav>
    <div class="abs search-btn">
      <svg width="28" height="28" viewBox="0 0 28 28"><circle cx="12.5" cy="12.5" r="5" fill="none" stroke="#fff" stroke-width="2"/><line x1="16" y1="16" x2="20" y2="20" stroke="#fff" stroke-width="2.4"/></svg>
    </div>
  </header>
  <div class="abs arrow" style="left:17px">
    <svg width="36" height="36" viewBox="0 0 36 36"><polyline points="21,11 14,18 21,25" fill="none" stroke="#fff" stroke-width="3"/></svg>
  </div>
  <div class="abs arrow" style="left:1147px">
    <svg width="36" height="36" viewBox="0 0 36 36"><polyline points="15,11 22,18 15,25" fill="none" stroke="#fff" stroke-width="3"/></svg>
  </div>

  <!-- subsidiaries band -->
  <section class="abs band">
    <div class="abs band-tab current" style="left:80px">T. M. Designs
      <svg width="26" height="24" viewBox="0 0 26 24" fill="none" stroke="#fff" stroke-width="1.6"><polygon points="13,3 25,9 13,15 1,9"/><path d="M6 12v6c4 3 10 3 14 0v-6"/><line x1="24" y1="9" x2="24" y2="16"/></svg>
    </div>
    <div class="abs band-tab" style="left:284px">T. M. Style
      <svg width="26" height="24" viewBox="0 0 26 24" fill="none" stroke="#fff" stroke-width="1.6"><rect x="2" y="10" width="5" height="12"/><path d="M7 11l5-8c2 0 3 1 3 3l-1 4h7c2 0 3 2 2 4l-2 7c-1 1-2 1-3 1H7"/></svg>
    </div>
    <div class="abs band-tab" style="left:490px">VERN LOUNGE
      <svg width="26" height="24" viewBox="0 0 26 24" fill="none" stroke="#fff" stroke-width="1.6"><polygon points="2,11 24,2 18,22 12,15"/><line x1="24" y1="2" x2="12" y2="15"/></svg>
    </div>
    <div class="abs band-tab" style="left:694px">VERN SUITES
      <svg width="26" height="24" viewBox="0 0 26 24" fill="none" stroke="#fff" stroke-width="1.6"><path d="M3 9l2-6h16l2 6z"/><path d="M4 9v13h18V9"/><rect x="10" y="14" width="6" height="8"/></svg>
    </div>
    <div class="abs band-tab" style="left:900px">THE MATERIAL NOOK
      <svg width="26" height="24" viewBox="0 0 26 24" fill="none" stroke="#fff" stroke-width="1.6"><circle cx="13" cy="12" r="4"/><circle cx="13" cy="12" r="9" stroke-dasharray="4 2.5"/></svg>
    </div>
  </section>

  <!-- about -->
  <h1 class="abs about-title">KALDRA HOLDINGS, LLC</h1>
  <p class="abs about-text" style="top:736px">KALDRA HOLDINGS, LLC is a Nevada corporation that brings together a family of design, style and hospitality businesses. T. M. Designs delivers interior design for commercial, residential and hospitality spaces, while T. M. Style offers fashion design and personal styling. THE MATERIAL NOOK distributes building and interior design materials to trade and private clients alike, from first sketch to final finish.</p>
  <p class="abs about-text" style="top:832px">In Accra, Ghana, VERN LOUNGE is an upscale membership only lounge serving business men and women, and VERN SUITES provides full service executive suites for top businesses. Visit www.kaldraholdingsllc.example, call 1 702-555-0147 in Las Vegas or +233 26 5550193 in Ghana.</p>

  <!-- offer -->
  <section class="abs offer">
    <h2 class="abs offer-title">WE OFFER<br>YOU</h2>
    <div class="abs offer-item" style="top:53px">
      <div class="offer-icon"><svg width="26" height="26" viewBox="0 0 26 26" fill="none" stroke="#fff" stroke-width="1.6"><rect x="7" y="2" width="12" height="22" rx="2"/><line x1="11" y1="20" x2="15" y2="20"/></svg></div>
      <h3>Interior Designs</h3>
      <p>T. M. Designs plans commercial, residential and hospitality interiors, from concept and layout to the finished space.</p>
    </div>
    <div class="abs offer-item" style="top:161px">
      <div class="offer-icon"><svg width="26" height="26" viewBox="0 0 26 26" fill="none" stroke="#fff" stroke-width="1.6"><ellipse cx="13" cy="5" rx="8" ry="3"/><path d="M5 5v16c0 2 4 3 8 3s8-1 8-3V5"/><path d="M5 11c0 2 4 3 8 3s8-1 8-3M5 16c0 2 4 3 8 3s8-1 8-3"/></svg></div>
      <h3>Fashion &amp; Styling</h3>
      <p>T. M. Style creates fashion designs and personal styling for clients who want a confident, polished look.</p>
    </div>
    <div class="abs offer-item" style="top:269px">
      <div class="offer-icon"><svg width="26" height="26" viewBox="0 0 26 26" fill="none" stroke="#fff" stroke-width="1.8"><path d="M18 8L9 17a2.5 2.5 0 0 0 3.5 3.5l10-10a4.5 4.5 0 0 0-6.4-6.4L5.5 14.7a6.3 6.3 0 0 0 9 9L22 16"/></svg></div>
      <h3>Design Materials</h3>
      <p>THE MATERIAL NOOK supplies building and interior design materials, with lounge and suites in Accra, Ghana.</p>
    </div>
  </section>

  <!-- contact -->
  <section class="abs contact" role="img" aria-label="Faded photo of the loft interior behind a slate grey overlay">
    <h2 style="top:12px;font-size:28px">CONTACT US</h2>
    <h2 style="top:48px;font-size:27px;font-weight:700">IT IS ALL ABOUT US</h2>

    <div class="abs contact-col" style="left:77px">
      <svg width="100" height="128" viewBox="0 0 100 128"><path d="M50 2C24 2 4 22 4 48c0 30 46 78 46 78s46-48 46-78C96 22 76 2 50 2z" fill="var(--teal)"/><circle cx="50" cy="46" r="16" fill="#5b6873"/></svg>
      <div class="bar"></div>
      <h4>Address</h4>
      <p>Las Vegas, Nevada / Accra, Ghana</p>
    </div>
    <div class="abs contact-col" style="left:430px">
      <svg width="200" height="128" viewBox="0 0 200 128" fill="none" stroke="var(--teal)" stroke-width="10"><rect x="6" y="14" width="188" height="108" rx="14"/><polyline points="16,26 100,86 184,26"/><line x1="16" y1="112" x2="76" y2="68"/><line x1="184" y1="112" x2="124" y2="68"/></svg>
      <div class="bar"></div>
      <h4>Mail</h4>
      <p>info@kaldraholdingsllc.example</p>
    </div>
    <div class="abs contact-col" style="left:787px">
      <svg width="90" height="128" viewBox="0 0 90 128" fill="none" stroke="var(--teal)" stroke-width="7"><rect x="6" y="4" width="78" height="120" rx="12"/><line x1="6" y1="22" x2="84" y2="22"/><line x1="6" y1="100" x2="84" y2="100"/><line x1="38" y1="112" x2="52" y2="112"/></svg>
      <div class="bar"></div>
      <h4>Phone</h4>
      <p>1 702-555-0147 · +233 26 5550193</p>
    </div>

    <div class="abs btn btn-line">Drop us a line</div>
    <div class="abs field" style="left:82px;top:525px;width:683px;height:43px">Name</div>
    <div class="abs field" style="left:82px;top:588px;width:683px;height:43px">E-mail</div>
    <div class="abs field" style="left:794px;top:525px;width:329px;height:108px">Message</div>
    <div class="abs btn btn-send">Drop us a line</div>
  </section>

  <!-- footer -->
  <footer class="abs footer">
    <h5 style="left:82px">Subscribe to our <b>NEWSLETTER</b></h5>
    <p class="abs news-text">Praesent vulputate, est rutrum volutpat placerat, metus arcu lobortis massa, quis vehicula ligula ipsum at ipsum.</p>
    <div class="abs news-input">E-mail address</div>
    <div class="abs btn news-btn">Subscribe</div>
    <div class="abs social"><span></span><span></span><span></span><span></span><span></span><span></span><span></span><span></span></div>

    <h5 style="left:616px">Our <b>MENU</b></h5>
    <nav class="menu">
      <a style="left:616px;top:100px">Home</a>
      <a style="left:616px;top:137px">Our Projects</a>
      <a style="left:616px;top:173px">About Us</a>
      <a style="left:616px;top:210px">Contact</a>
      <a style="left:735px;top:100px">Blog</a>
      <a style="left:735px;top:137px">Our Team</a>
      <a style="left:735px;top:173px">Features</a>
      <a style="left:735px;top:210px">Services</a>
    </nav>

    <h5 style="left:882px">Latest <b>TWEETS</b></h5>
    <div class="abs tweet-dot" style="left:884px;top:101px"></div>
    <p class="abs tweet" style="top:97px">Here goes some twitter feeds from your twitter profiles. Lorem ipsum is demo text. #Kaldra #Holdings kaldra.example/wpr 4 DAYS AGO</p>
    <div class="abs tweet-dot" style="left:884px;top:185px"></div>
    <p class="abs tweet" style="top:181px">Here goes some twitter feeds from your twitter profiles. Lorem ipsum is demo text. #Kaldra #Holdings kaldra.example/wpr 4 DAYS AGO</p>
  </footer>

</div>
</body>
</html>
```